Web Design Project - vR Advise

We want to modernise our web page profile. We have an existing web site that we are particularly not proud of (www.vradvise.com.au).
We have started to build a new web site using Joomla and we like the structure of it, but we need it to be professionally designed and implemented.

This current development site can be viewed here: dev.vradvise.com.au

We would like a complete design for the entire website, ready for deployment.

(We still need to finalise the content, as we have just developed new products that we hope to launch in August both on this web site and by a Vendor Forum.)
Updates

Target Market(s)

Larger companies where the robustness of their IT infrastructure is critical. Our tools and services provide for monitoring of every device

Industry/Entity Type

Build

Requirements
Must have
• Responsive design for different screen sizes.

BrightDock help desk software integrated with the website.
Currently can be viewed at support.vradvise.com.au
Brightdock only supports custom css.

Nice to have
• Customer experience testimonials in a rotating banner
Chirpr and Pagebook links in the footer
We use Avenir as a company font.
Use company colours as in the logo (green and blue)

```html
<!DOCTYPE html>
<html lang="en">
<head>
<meta charset="utf-8">
<title>vR Advise – Home</title>
<link rel="stylesheet" href="https://fonts.googleapis.com/css2?family=Montserrat:wght@600;700;800&family=Mulish:wght@400;600;700&display=swap">
<style>
:root{
  --blue:#2c6ea8;
  --blue-dark:#225a8c;
  --blue-light:#3a8fd0;
  --green:#97bf1e;
  --green-light:#b5d53a;
  --text:#6b6f73;
  --hero-top:#dbe9f2;
  --hero-bottom:#c9e0ee;
  --band:#eef1f3;
  --white:#ffffff;
}
*{box-sizing:border-box;margin:0;padding:0}
html,body{width:1200px;height:961px;overflow:hidden;background:#fff}
body{font-family:"Mulish",sans-serif;color:var(--text)}
.page{position:relative;width:1200px;height:961px;overflow:hidden;background:linear-gradient(#fdfdfd,#f3f4f5)}
.abs{position:absolute}

.top-strip{left:0;top:0;width:1200px;height:7px;background:var(--blue)}
.hero{left:0;top:7px;width:1200px;height:375px;background:linear-gradient(135deg,#d6e7f1 0%,#eef5f9 45%,var(--hero-bottom) 100%)}
.utility-tab{left:858px;top:7px;width:138px;height:21px;background:var(--blue);display:flex;align-items:center;justify-content:space-around;padding:0 10px}
.utility-tab::before{content:"";position:absolute;left:-12px;top:0;border-top:21px solid var(--green);border-left:12px solid transparent}
.social{display:flex;gap:4px}
.social span{width:21px;height:21px;border-radius:50%;display:block}
.social .s1{background:#3ea9e0}.social .s2{background:#2b5fa5}.social .s3{background:#3b3b3b}
.social.top{left:922px;top:45px}

.brand{left:208px;top:62px;display:flex;align-items:center;gap:10px}
.brand-dot{width:34px;height:34px;border-radius:50%;background:var(--green)}
.brand-name{font-family:"Montserrat",sans-serif;font-weight:700;font-size:34px;color:var(--blue)}

.nav{left:553px;top:78px;display:flex;font-family:"Montserrat",sans-serif;font-weight:600;font-size:13px;color:var(--blue)}
.nav a{color:inherit;text-decoration:none;padding:0 8px 8px;border-right:1px dotted #8fb1cc;line-height:13px}
.nav a:last-child{border-right:0}
.nav a.current{border-bottom:3px solid var(--blue)}
.nav-rule{left:480px;top:104px;width:540px;height:1px;background:linear-gradient(90deg,transparent,#b7c9d6,transparent)}

.hero-title{left:202px;top:164px;font-family:"Montserrat",sans-serif;font-weight:800;font-size:25px;line-height:27px;letter-spacing:-1px;color:var(--blue)}
.hero-title em{font-style:normal;color:var(--green)}
.hero-copy{left:202px;top:260px;width:340px;font-size:9.5px;line-height:16.5px;text-transform:uppercase;color:#6f7477}
.btn-quote{left:198px;top:323px;width:172px;height:33px;border-radius:17px;background:linear-gradient(var(--green-light),var(--green));box-shadow:0 0 0 3px rgba(255,255,255,.7);color:#fff;font-family:"Montserrat",sans-serif;font-weight:700;font-size:11.5px;display:flex;align-items:center;padding-left:21px}
.btn-quote svg{position:absolute;right:12px;top:9px}
.btn-quote::after{content:"";position:absolute;right:38px;top:4px;width:1px;height:25px;background:rgba(255,255,255,.4)}
.hero-visual{left:552px;top:112px;width:456px;height:270px;background:radial-gradient(ellipse at 62% 40%,#f5f7f8 0%,#e3ecf1 45%,rgba(205,225,237,0) 75%)}

.lead-band{left:0;top:382px;width:1200px;height:54px;background:linear-gradient(#fafafa,#e4e6e8);border-top:1px solid #cfd5d9}
.field{top:396px;height:27px;display:flex;border:1px solid #d4d8db;background:#fff}
.field .ico{width:37px;background:var(--blue);display:flex;align-items:center;justify-content:center}
.field .ph{font-size:9px;color:#a5a9ad;padding:0 13px;line-height:25px;text-transform:uppercase;letter-spacing:.3px}
.f1{left:197px;width:174px}.f2{left:414px;width:176px}.f3{left:627px;width:174px}
.sep{top:402px;width:1px;height:16px;border-left:1px dotted #9aa0a4}
.btn-submit{left:844px;top:394px;width:136px;height:31px;border-radius:16px;background:linear-gradient(var(--green-light),var(--green));box-shadow:0 0 0 3px rgba(255,255,255,.8);color:#fff;font-family:"Montserrat",sans-serif;font-weight:700;font-size:14px;text-align:center;line-height:31px}

.service{top:488px;width:250px}
.service .head{display:flex;align-items:center;gap:10px;height:46px}
.service .head svg{flex:none}
.service h2{font-family:"Montserrat",sans-serif;font-weight:700;font-size:14px;line-height:17px;color:var(--blue);border-left:1px dotted #9aa0a4;padding-left:9px}
.service p{margin-top:13px;font-size:10.5px;line-height:14.4px;color:#777b7f}
.btn-more{display:inline-block;margin-top:9px;width:72px;height:22px;border-radius:11px;background:var(--blue);color:#fff;font-family:"Montserrat",sans-serif;font-weight:700;font-size:8px;text-align:center;line-height:22px}
.s1c{left:198px}.s2c{left:475px}.s3c{left:750px;width:250px}

.testimonials{left:0;top:652px;width:1200px;height:144px;border-top:1px solid #e9eaeb;background:linear-gradient(#fbfbfb,#f2f3f4)}
.quote{top:686px;width:245px;height:78px}
.avatar{position:absolute;left:0;top:0;width:76px;height:76px;border-radius:50%;border:4px solid #fff;box-shadow:0 1px 4px rgba(0,0,0,.3);background:radial-gradient(circle at 50% 40%,#e8d6c8,#b89a86 60%,#d7dbde)}
.bubble{position:absolute;left:72px;top:16px;width:150px;height:27px;background:var(--blue-light);color:#e6f1fa;font-size:8.5px;line-height:10.5px;padding:4px 0 0 8px}
.qmark{position:absolute;left:227px;top:17px;width:15px;height:15px;background:#fff;border:1px solid #cfd5d9;color:var(--blue);font-family:"Montserrat",sans-serif;font-weight:800;font-size:13px;line-height:17px;text-align:center}
.meta{position:absolute;left:72px;top:43px;width:150px;height:17px;background:#fff;border:1px solid #d8dcdf;display:flex;align-items:center;gap:5px;padding-left:6px;font-family:"Montserrat",sans-serif;font-weight:700;font-size:8px;color:#222}
.meta .stars{color:#e4b64a;font-size:8px;letter-spacing:-.5px;border-left:1px dotted #999;padding-left:4px}
.q1{left:198px}.q2{left:476px}.q3{left:754px}

.partners{left:0;top:798px;width:1200px;height:60px;background:linear-gradient(#f7f7f7,#e6e8ea);border-top:1px solid #d8dcdf}
.partners h3{position:absolute;left:202px;top:18px;font-family:"Montserrat",sans-serif;font-weight:800;font-size:20px;letter-spacing:-.8px;color:var(--blue)}
.partner-divider{left:382px;top:808px;width:1px;height:42px;background:#cfd3d6}
.badge{top:0;background:#bfc6cc}
.pb1{left:421px;top:806px;width:26px;height:40px;border-radius:2px;background:#2d3b70}
.pb2{left:515px;top:814px;width:118px;height:28px;border-radius:4px;background:#3a74a9}
.pb3{left:697px;top:818px;width:105px;height:20px;border-radius:4px;background:#8b8f93}
.pb4{left:875px;top:810px;width:92px;height:36px;border-radius:4px;background:#23407a}

.footer{left:0;top:858px;width:1200px;height:103px;background:var(--blue);color:#fff}
.footer h4{position:absolute;font-family:"Montserrat",sans-serif;font-weight:700;font-size:14px;letter-spacing:-.3px}
.f-about{left:199px;top:20px}
.f-about-copy{left:198px;top:41px;width:200px;font-size:9.5px;line-height:11.5px;color:#e3eef7}
.f-links{left:198px;top:79px;font-size:9.5px;color:#e3eef7}
.f-connect{left:544px;top:17px}
.social.foot{left:571px;top:39px}
.f-rights{left:611px;top:79px;font-size:9.5px;color:#e3eef7}
.f-contact{left:822px;top:20px}
.f-role{left:823px;top:40px;font-family:"Montserrat",sans-serif;font-weight:600;font-size:10px;letter-spacing:.2px}
.f-table{left:822px;top:55px;font-size:9.5px;line-height:11.5px;display:grid;grid-template-columns:46px auto;color:#eef5fa}
</style>
</head>
<body>
<div class="page">
  <div class="abs hero"></div>
  <div class="abs top-strip"></div>

  <div class="abs utility-tab">
    <svg width="14" height="12" viewBox="0 0 14 12"><path d="M1 6 7 1l6 5M3 5v6h8V5" fill="none" stroke="#fff" stroke-width="1.5"/></svg>
    <svg width="14" height="10" viewBox="0 0 14 10"><rect x="1" y="1" width="12" height="8" fill="none" stroke="#fff" stroke-width="1.3"/><path d="M1 1l6 5 6-5" fill="none" stroke="#fff" stroke-width="1.3"/></svg>
    <svg width="14" height="12" viewBox="0 0 14 12"><rect x="1" y="1" width="12" height="10" rx="1" fill="none" stroke="#fff" stroke-width="1.3"/><rect x="3" y="3" width="4" height="6" fill="#fff"/></svg>
    <svg width="12" height="12" viewBox="0 0 12 12"><circle cx="6" cy="6" r="5.5" fill="#e9eef2"/><rect x="1" y="3" width="10" height="1.3" fill="#d04444"/><rect x="1" y="6" width="10" height="1.3" fill="#d04444"/><rect x="2" y="8.8" width="8" height="1.2" fill="#d04444"/><rect x="1.5" y="1.5" width="4.5" height="4" fill="#3a5a9a"/></svg>
  </div>

  <div class="abs social top"><span class="s1"></span><span class="s2"></span><span class="s3"></span></div>

  <div class="abs brand"><span class="brand-dot"></span><span class="brand-name">vR Advise</span></div>

  <nav class="abs nav">
    <a class="current">HOME</a><a>SERVICES</a><a>SOLUTIONS</a><a>PARTNERS</a><a>ABOUT US</a><a>CONTACT</a>
  </nav>
  <div class="abs nav-rule"></div>

  <h1 class="abs hero-title">DEDICATED TO MAKING<br>BUSINESS SENSE OF <em>IT</em><br>CHALLENGES.</h1>
  <p class="abs hero-copy">We are an organisation that prides itself on attracting, employing, retaining and developing subject matter experts in the field of consulting.</p>
  <div class="abs btn-quote">REQUEST A QUOTE<svg width="9" height="15" viewBox="0 0 9 15"><path d="M1 1l6.5 6.5L1 14" fill="none" stroke="#fff" stroke-width="1.6"/></svg></div>

  <div class="abs hero-visual" role="img" aria-label="Smiling consultant in white shirt and tie holding a globe surrounded by networked laptops"></div>

  <div class="abs lead-band"></div>
  <div class="abs field f1"><div class="ico"><svg width="12" height="13" viewBox="0 0 12 13"><circle cx="6" cy="4" r="3" fill="#fff"/><path d="M0 13c0-4 3-5 6-5s6 1 6 5z" fill="#fff"/></svg></div><div class="ph">Enter your name</div></div>
  <div class="abs sep" style="left:393px"></div>
  <div class="abs field f2"><div class="ico"><svg width="15" height="10" viewBox="0 0 15 10"><rect x="1" y="1" width="13" height="8" fill="none" stroke="#fff" stroke-width="1.3"/><path d="M1 1l6.5 5 6.5-5" fill="none" stroke="#fff" stroke-width="1.3"/></svg></div><div class="ph">Your email adderess</div></div>
  <div class="abs sep" style="left:608px"></div>
  <div class="abs field f3"><div class="ico"><svg width="15" height="12" viewBox="0 0 15 12"><rect x="1" y="1" width="13" height="10" rx="1" fill="none" stroke="#fff" stroke-width="1.3"/><rect x="3" y="3" width="4" height="6" fill="#fff"/><rect x="9" y="3" width="3" height="2" fill="#fff"/></svg></div><div class="ph">Your phone number</div></div>
  <div class="abs sep" style="left:822px;top:392px;height:38px;border-left:1px solid #d0d4d7"></div>
  <div class="abs btn-submit">SUBMIT NOW</div>

  <section class="abs service s1c">
    <div class="head">
      <svg width="48" height="42" viewBox="0 0 48 42"><circle cx="18" cy="12" r="9" fill="var(--blue)"/><path d="M2 42c0-13 7-17 16-17s16 4 16 17z" fill="var(--blue)"/><circle cx="36" cy="16" r="7" fill="none" stroke="var(--green)" stroke-width="3"/><path d="M30 22l-4 5 7-2" fill="var(--green)"/></svg>
      <h2>IT CONSULTING<br>SERVICES</h2>
    </div>
    <p>Lorem ipsum dolor sit amet, consectetuer adipiscing elit, sed diam nonummy nibh euismod tincidunt ut laoreet dolore.</p>
    <span class="btn-more">READ MORE</span>
  </section>

  <section class="abs service s2c">
    <div class="head">
      <svg width="48" height="46" viewBox="0 0 48 46"><rect x="0" y="0" width="3" height="46" fill="var(--blue)"/><rect x="6" y="9" width="36" height="3" fill="var(--blue)"/><rect x="6" y="21" width="36" height="3" fill="var(--blue)"/><rect x="6" y="33" width="36" height="3" fill="var(--blue)"/><circle cx="22" cy="10.5" r="4" fill="var(--green)"/><circle cx="34" cy="22.5" r="4" fill="var(--green)"/><circle cx="16" cy="34.5" r="4" fill="var(--green)"/></svg>
      <h2>IT ARCHITECTURE<br>SERVICES</h2>
    </div>
    <p>Lorem ipsum dolor sit amet, consectetuer adipiscing elit, sed diam nonummy nibh euismod tincidunt ut laoreet dolore.</p>
    <span class="btn-more">READ MORE</span>
  </section>

  <section class="abs service s3c">
    <div class="head">
      <svg width="48" height="46" viewBox="0 0 48 46"><path d="M2 24C3 10 13 3 24 3s21 7 22 21c-4-3-8-3-11 0-3-3-8-3-11 0-3-3-8-3-11 0-3-3-8-3-11 0z" fill="var(--green)"/><rect x="23" y="0" width="2" height="4" fill="var(--blue)"/><path d="M24 24v15a4 4 0 0 1-8 0" fill="none" stroke="var(--blue)" stroke-width="3"/></svg>
      <h2>PROFESSIONAL SERVICE<br>AND SUPPORT</h2>
    </div>
    <p>Lorem ipsum dolor sit amet, consectetuer adipiscing elit, sed diam nonummy nibh euismod tincidunt ut laoreet dolore.</p>
    <span class="btn-more">READ MORE</span>
  </section>

  <div class="abs testimonials"></div>
  <figure class="abs quote q1">
    <div class="avatar" role="img" aria-label="Portrait photo of a client"></div>
    <div class="bubble">Lorem ipsum dolor sit amet,<br>consectetuer adipiscing elit, sed.</div>
    <div class="qmark">”</div>
    <div class="meta"><svg width="8" height="9" viewBox="0 0 8 9"><circle cx="4" cy="2.5" r="2.3" fill="var(--blue)"/><path d="M0 9c0-3 2-4 4-4s4 1 4 4z" fill="var(--blue)"/></svg>LOREM IPSUM<span class="stars">★★★★★★</span></div>
  </figure>
  <figure class="abs quote q2">
    <div class="avatar" role="img" aria-label="Portrait photo of a client"></div>
    <div class="bubble">Lorem ipsum dolor sit amet,<br>consectetuer adipiscing elit, sed.</div>
    <div class="qmark">”</div>
    <div class="meta"><svg width="8" height="9" viewBox="0 0 8 9"><circle cx="4" cy="2.5" r="2.3" fill="var(--blue)"/><path d="M0 9c0-3 2-4 4-4s4 1 4 4z" fill="var(--blue)"/></svg>LOREM IPSUM<span class="stars">★★★★★★</span></div>
  </figure>
  <figure class="abs quote q3">
    <div class="avatar" role="img" aria-label="Portrait photo of a client"></div>
    <div class="bubble">Lorem ipsum dolor sit amet,<br>consectetuer adipiscing elit, sed.</div>
    <div class="qmark">”</div>
    <div class="meta"><svg width="8" height="9" viewBox="0 0 8 9"><circle cx="4" cy="2.5" r="2.3" fill="var(--blue)"/><path d="M0 9c0-3 2-4 4-4s4 1 4 4z" fill="var(--blue)"/></svg>LOREM IPSUM<span class="stars">★★★★★★</span></div>
  </figure>

  <div class="abs partners"><h3>OUR PARTNERS:</h3></div>
  <div class="abs partner-divider"></div>
  <div class="abs pb1" role="img" aria-label="Partner badge"></div>
  <div class="abs pb2" role="img" aria-label="Partner badge"></div>
  <div class="abs pb3" role="img" aria-label="Partner badge"></div>
  <div class="abs pb4" role="img" aria-label="Partner badge"></div>

  <footer class="abs footer">
    <h4 class="f-about">ABOUT US</h4>
    <p class="abs f-about-copy">Lorem ipsum dolor sit amet, consectetuer adipiscing elit, sed diam nonummy nibh euismod tincidunt.</p>
    <p class="abs f-links">HOME | ABOUT US | PATENT PENDING | COPY RIGHT | PRIVACY | CONTACT US PRIVACY</p>
    <h4 class="f-connect">CONNECT WITH US</h4>
    <div class="abs social foot"><span class="s1"></span><span class="s2"></span><span class="s3"></span></div>
    <p class="abs f-rights">2013 VR ADVISE, ALL RIGHTS RESERVED.</p>
    <h4 class="f-contact">DANA MORROW</h4>
    <p class="abs f-role">SALES &amp; MARKETING DIRECTOR</p>
    <div class="abs f-table">
      <span>Mobile:</span><span>+61 (0) 400 555 12</span>
      <span>Email:</span><span>danamorrow@vradvise.com.au</span>
      <span>Web:</span><span>www.vradvise.com.au</span>
    </div>
  </footer>
</div>
</body>
</html>
```